design a catchy flyer for my electrical buisness

need a flyer designed to attract people to my business by looking professional and offering specials

Target Market(s)

all people i want to look affordable to everyone but still keeping that professional look and feel

Industry/Entity Type

Electrical

Requirements
Must have
• NO JOB TO BIG OR SMALL
• CALL NOW FOR A FREE QUOTE 0400318726
• NO CALL OUT FEE
• same promises as uploaded pic maybe written different style
• Your neighborhood electrician
• 100% satisfaction guaranteed
• were here to help
• mention this flyer for 10% off
• specializing in house renovations, extensions, kitchen and bathroom upgrades switchboard upgrades
• Make your house safe with our RCD and smoke alarm packages
Nice to have
• modern
• proffesional
• shows trust when customers read it
Should not have
• corny slogans
• cheap look

```html
<!DOCTYPE html>
<html lang="en">
<head>
<meta charset="utf-8">
<title>Your Neighborhood Electrician – VoltWise</title>
<link href="https://fonts.googleapis.com/css2?family=Noto+Serif:wght@400;700&family=Open+Sans:wght@400;600&display=swap" rel="stylesheet">
<style>
  :root{
    --orange:#f39a4c;
    --orange-deep:#e9833a;
    --charcoal:#3d3d3f;
    --charcoal-dark:#2f2f31;
    --ink:#1c1c1c;
    --paper:#ffffff;
    --cream:#fdf4ec;
    --ring:#f6b27a;
  }
  *{margin:0;padding:0;box-sizing:border-box}
  html,body{width:851px;height:1200px;overflow:hidden;background:var(--paper)}
  .flyer{position:relative;width:851px;height:1200px;background:var(--cream);font-family:"Noto Serif",Georgia,serif;color:var(--ink);overflow:hidden}

  .hero{position:absolute;left:0;top:0;width:851px;height:420px;background:var(--paper)}
  .headline{position:absolute;left:84px;top:70px;font-family:"Open Sans",Arial,sans-serif;font-size:40px;line-height:62px;font-weight:400;color:var(--charcoal-dark)}
  .brand{position:absolute;left:84px;top:300px;display:flex;align-items:center;gap:16px}
  .brand-mark{width:46px;height:46px;border-radius:50%;background:var(--orange)}
  .brand-name{font-family:"Open Sans",Arial,sans-serif;font-size:30px;font-weight:600;color:var(--orange-deep)}

  .benefit-band{position:absolute;left:0;top:420px;width:851px;height:162px;background:var(--orange)}

  .technician-photo{position:absolute;left:510px;top:0;width:315px;height:570px;
    background:linear-gradient(180deg,#d9c2ad 0%,#8ea0c8 30%,#3f56a3 60%,#2c3f86 100%)}

  .badge{position:absolute;top:408px;width:150px;height:150px;border-radius:50%;background:var(--charcoal);
    border:4px solid var(--ring);display:flex;align-items:center;justify-content:center;text-align:center;
    color:var(--paper);font-size:19px;font-weight:700;line-height:1.3;padding:14px}
  .badge.one{left:138px}
  .badge.two{left:350px}
  .badge.three{left:563px}

  .promises{position:absolute;left:58px;top:598px;width:760px}
  .promises h2{font-size:22px;font-weight:700;line-height:34px;color:var(--ink)}
  .promises ul{list-style:none}
  .promises li{display:flex;align-items:center;gap:16px;font-size:22px;font-weight:700;line-height:37px}
  .tick{width:20px;height:20px;flex:none}

  .call-band{position:absolute;left:0;top:860px;width:851px;height:161px;background:var(--charcoal);color:var(--paper);padding:18px 0 0 32px}
  .call-line{font-family:"Open Sans",Arial,sans-serif;font-size:42px;font-weight:400;line-height:58px;white-space:nowrap}
  .offer-line{font-size:54px;font-weight:400;line-height:70px;white-space:nowrap}

  .services{position:absolute;left:0;top:1021px;width:851px;height:37px;background:var(--paper);
    font-size:16.5px;white-space:nowrap;display:flex;align-items:center;justify-content:center}
  .safety{position:absolute;left:0;top:1058px;width:851px;height:42px;background:var(--orange);
    font-size:16px;white-space:nowrap;display:flex;align-items:center;justify-content:center}
  .foot{position:absolute;left:0;top:1100px;width:851px;height:100px;background:var(--paper)}
</style>
</head>
<body>
<div class="flyer">
  <section class="hero">
    <h1 class="headline">Your<br>Neighborhood<br>Electrician</h1>
    <div class="brand">
      <span class="brand-mark"></span>
      <span class="brand-name">VoltWise</span>
    </div>
  </section>

  <section class="benefit-band"></section>

  <div class="technician-photo" role="img" aria-label="Smiling electrician in blue overalls carrying a coil of cable over his shoulder"></div>

  <div class="badge one">No job too big or too small!</div>
  <div class="badge two">100% satisfaction guaranteed!</div>
  <div class="badge three">No call out fee!</div>

  <section class="promises">
    <h2>We're Here To Help And Here's Our Promise To You:</h2>
    <ul>
      <li><svg class="tick" viewBox="0 0 24 24"><path d="M3 13l6 6L21 5" fill="none" stroke="#1c1c1c" stroke-width="3.4" stroke-linecap="round" stroke-linejoin="round"/></svg>We're on time or you get $100</li>
      <li><svg class="tick" viewBox="0 0 24 24"><path d="M3 13l6 6L21 5" fill="none" stroke="#1c1c1c" stroke-width="3.4" stroke-linecap="round" stroke-linejoin="round"/></svg>You know how much you'll pay before we start</li>
      <li><svg class="tick" viewBox="0 0 24 24"><path d="M3 13l6 6L21 5" fill="none" stroke="#1c1c1c" stroke-width="3.4" stroke-linecap="round" stroke-linejoin="round"/></svg>Fixed price guarantee</li>
      <li><svg class="tick" viewBox="0 0 24 24"><path d="M3 13l6 6L21 5" fill="none" stroke="#1c1c1c" stroke-width="3.4" stroke-linecap="round" stroke-linejoin="round"/></svg>We'll leave your home as clean as when we arrived</li>
      <li><svg class="tick" viewBox="0 0 24 24"><path d="M3 13l6 6L21 5" fill="none" stroke="#1c1c1c" stroke-width="3.4" stroke-linecap="round" stroke-linejoin="round"/></svg>If we make a mistake, we fix it for free</li>
      <li><svg class="tick" viewBox="0 0 24 24"><path d="M3 13l6 6L21 5" fill="none" stroke="#1c1c1c" stroke-width="3.4" stroke-linecap="round" stroke-linejoin="round"/></svg>Calls are always returned right away</li>
    </ul>
  </section>

  <section class="call-band">
    <p class="call-line">Call Now For&nbsp; Free Quote: 0400 318 726</p>
    <p class="offer-line">Mention this flyer for 10% off</p>
  </section>

  <p class="services">Specializing in house renovations, extensions, kitchen and bathroom upgrades switchboard upgrades</p>
  <p class="safety">Make your house safe with our RCD and smoke alarm packages</p>
  <div class="foot"></div>
</div>
</body>
</html>
```